KVT Wellness Co Business Card for food and Beverage Falcons & Lanterns

One main business card design for a wellness enterprise which represents two brands. We need one primary card design, for two different employees. The only difference between the cards will be the name, title and phone number for each employee, all other design elements will be same.
I've uploaded the logos for each brand. I have also uploaded a mockup which I made using Google's drawing tool. I can provide example images of business cards we find attractive if you would like some help picturing what we like.
I'm picturing the color splash on the back of the card below the two logos to be a dark burgundy or blue. This may sound a bit silly but the feel of the card and color should look almost like wizard dress robes. Dark emerald green, dark blue and dark burgundy with black undertones and gold lace.
Updates

Reason: Thank you all for the submissions. I will need some extra time to give you feedback. Cheers

Target Market(s)

Healthy food and beverage industry

Industry/Entity Type

Health And Wellness

Contact Information for Business Card

On one side we would like the business name, location, title of employee, employee name and contact details. On the flip side we would like our two brand logos and a splash of color. We would like the card to have a black font with some gold accents if possible. We would also like the trim of the business card or a middle ply within the card stock to have a color other than white.

Font styles to use
Serif

Colors
ec1f27
0255a3
00a990

Requirements
Must have
• Bold dark colors, happy to provide sample photos of business cards I like from clipnook. Must have a version for two different employees. Must be sharp, modern and chic.
Nice to have
• Thick card stock layer in between the front and back of card that is either black or gold lace or something to make it feel, well let's say to make it feel expensive.
Should not have
• Should not have any cartoon-ey elements. All business.

```html
<!DOCTYPE html>
<html lang="en">
<head>
<meta charset="utf-8">
<title>KVT Wellness Co – Business Card</title>
<link rel="stylesheet" href="https://fonts.googleapis.com/css2?family=Cinzel:wght@400;600;700&family=Crimson+Text:ital,wght@0,400;0,600;1,400&display=swap">
<style>
  :root {
    --backdrop: #2b2b2d;
    --card: #ffffff;
    --navy: #221f5e;
    --burgundy: #a8262a;
    --ink: #111111;
    --shadow: rgba(0, 0, 0, 0.45);
  }
  * { box-sizing: border-box; margin: 0; padding: 0; }
  html, body {
    width: 1200px;
    height: 852px;
    overflow: hidden;
    background: var(--backdrop);
  }
  .stage {
    width: 1200px;
    height: 852px;
    display: flex;
    align-items: center;
    justify-content: center;
    gap: 40px;
  }
  .card {
    position: relative;
    width: 540px;
    height: 309px;
    background: var(--card);
    border-radius: 18px;
    overflow: hidden;
    box-shadow: 0 14px 30px var(--shadow);
  }
  .card__wave {
    position: absolute;
    inset: 0;
    width: 100%;
    height: 100%;
  }
  .wave-navy { fill: var(--navy); }
  .wave-red { fill: var(--burgundy); }
  .wave-light { fill: var(--card); }

  /* Front */
  .contact {
    position: absolute;
    top: 34px;
    right: 44px;
    width: 300px;
    text-align: center;
    color: var(--ink);
  }
  .contact__company {
    font-family: "Cinzel", serif;
    font-weight: 700;
    font-size: 26px;
    letter-spacing: 1px;
    line-height: 1.1;
  }
  .contact__location {
    font-family: "Cinzel", serif;
    font-weight: 600;
    font-size: 15px;
    letter-spacing: 1px;
    margin-top: 4px;
  }
  .contact__divider {
    width: 22px;
    height: 5px;
    background: var(--burgundy);
    margin: 14px auto;
  }
  .contact__name {
    font-family: "Cinzel", serif;
    font-weight: 600;
    font-size: 17px;
    letter-spacing: 1px;
  }
  .contact__title,
  .contact__phone,
  .contact__email {
    font-family: "Crimson Text", serif;
    font-size: 14px;
    line-height: 1.35;
  }

  /* Back */
  .brand {
    position: absolute;
    font-family: "Cinzel", serif;
    font-weight: 700;
    font-size: 22px;
    letter-spacing: 1px;
    color: var(--ink);
    text-align: center;
    white-space: nowrap;
  }
  .brand--primary {
    top: 66px;
    right: 46px;
  }
  .brand--secondary {
    top: 138px;
    left: 150px;
  }
</style>
</head>
<body>
<main class="stage">

  <section class="card card--front" aria-label="Business card front">
    <svg class="card__wave" viewBox="0 0 540 309" aria-hidden="true">
      <path class="wave-red" d="M0,110 C135,120 255,190 326,309 L312,309 C242,200 122,136 0,124 Z"/>
      <path class="wave-navy" d="M0,140 C112,150 232,210 300,309 L0,309 Z"/>
    </svg>
    <div class="contact">
      <h1 class="contact__company">KVT WELLNESS CO</h1>
      <p class="contact__location">BROOKDALE, CA</p>
      <div class="contact__divider"></div>
      <p class="contact__name">MARCUS HALE</p>
      <p class="contact__title">Beverage Alchemist</p>
      <p class="contact__phone">415.555.0172</p>
      <div class="contact__divider"></div>
      <p class="contact__email">kvtwellnessco@mailhub.com</p>
    </div>
  </section>

  <section class="card card--back" aria-label="Business card back">
    <svg class="card__wave" viewBox="0 0 540 309" aria-hidden="true">
      <path class="wave-red" d="M40,196 C150,176 262,218 336,290 C258,234 152,196 40,204 Z"/>
      <path class="wave-navy" d="M0,214 C128,206 248,238 338,309 L0,309 Z"/>
      <path class="wave-light" d="M0,242 C108,230 226,252 314,309 L296,309 C212,264 104,246 0,254 Z"/>
    </svg>
    <p class="brand brand--primary">KVT Wellness Co</p>
    <p class="brand brand--secondary">Falcons &amp; Lanterns</p>
  </section>

</main>
</body>
</html>
```